Independent book publisher needs book cover design

We need a full book cover (front, back and spine) designed for one of our authors and a detailed specification doc is attached.

The book is titled, "Bracing for Storms, Charting Every Exit: Ways to build backup strategies; since readiness beats scrambling through wreckage later". It outlines a structured process by which women can avoid or reduce risk and uncertainty in their lives. It is written for women who have a lot to lose.

A good metaphor for this book would be one that is related to prevention or rescue. The author prefers something based on a lifeboat or perhaps an empty life preserver (maybe with sinking ship and sharks in background). Other ideas are welcomed.

Target Market(s)

It is written for women who have a lot to lose.

Industry/Entity Type

Book Publisher

Requirements
Must have
• See attachment.
• Please note:
• The uploaded file has been updated and a bar code file has been uploaded.

```html
<!DOCTYPE html>
<html lang="en">
<head>
<meta charset="utf-8">
<title>Bracing for Storms, Charting Every Exit — Full Cover</title>
<link rel="stylesheet" href="https://fonts.googleapis.com/css2?family=Oswald:wght@500;700&family=Roboto+Condensed:wght@400;700&display=swap">
<style>
  :root {
    --page: #ffffff;
    --wrap-navy: #3d4868;
    --panel-navy: #4c5a7d;
    --ink-white: #ffffff;
    --ink-black: #111111;
    --band-white: #f4f6f5;
    --sky-top: #4d6f94;
    --sky-mid: #9fb6c9;
    --horizon: #c9d6dc;
    --grass: #7e9a4a;
    --road: #3b3d40;
  }
  * { margin: 0; padding: 0; box-sizing: border-box; }
  html, body { width: 1200px; height: 999px; overflow: hidden; background: var(--page); }
  .canvas { position: relative; width: 1200px; height: 999px; }

  .back-cover {
    position: absolute; left: 25px; top: 98px; width: 593px; height: 802px;
    background: var(--wrap-navy);
  }
  .back-panel {
    position: absolute; left: 23px; top: 27px; width: 512px; height: 747px;
    background: var(--panel-navy); border-radius: 14px;
    font-family: "Roboto Condensed", "Arial Narrow", sans-serif;
    color: var(--ink-white);
  }
  .back-heading {
    position: absolute; left: 19px; top: 17px; width: 480px;
    font-size: 21.5px; font-weight: 700; letter-spacing: 0.1px; white-space: nowrap;
  }
  .back-copy {
    position: absolute; left: 19px; top: 54px; width: 485px;
    font-size: 12.4px; line-height: 16px; text-align: justify;
  }
  .back-copy p { margin-bottom: 16px; }
  .back-copy .lead { font-weight: 700; font-size: 13.6px; line-height: 17px; margin-bottom: 6px; }
  .topic-list { list-style: none; margin-bottom: 7px; }
  .topic-list li::before { content: "• "; }
  .author-bio {
    position: absolute; left: 19px; top: 492px; width: 336px;
    font-size: 12.4px; line-height: 16px; text-align: justify;
  }
  .author-photo {
    position: absolute; left: 366px; top: 492px; width: 131px; height: 156px;
    background: var(--ink-white); border-radius: 12px;
  }
  .barcode-space {
    position: absolute; left: 285px; top: 664px; width: 208px; height: 70px;
    background: var(--ink-white);
  }
  .website {
    position: absolute; left: 25px; top: 716px;
    font-size: 12.5px; font-weight: 700;
  }

  .spine {
    position: absolute; left: 560px; top: 98px; width: 58px; height: 802px;
    background: var(--wrap-navy);
  }
  .spine-title, .spine-author {
    position: absolute; left: 17px;
    writing-mode: vertical-rl;
    font-family: "Roboto Condensed", "Arial Narrow", sans-serif;
    font-weight: 700; color: var(--ink-white); font-size: 21px; white-space: nowrap;
  }
  .spine-title { top: 83px; }
  .spine-author { top: 612px; font-size: 22px; }

  .front-cover {
    position: absolute; left: 618px; top: 98px; width: 557px; height: 802px; overflow: hidden;
  }
  .cover-photo {
    position: absolute; inset: 0;
    background: linear-gradient(180deg, var(--sky-top) 0%, var(--sky-mid) 42%, var(--horizon) 60%, var(--grass) 66%, var(--road) 74%, #2c2e31 100%);
  }
  .front-title {
    position: absolute; left: 0; top: 30px; width: 557px; text-align: center;
    font-family: "Oswald", "Arial Narrow", sans-serif; font-weight: 700;
    color: var(--ink-white); text-transform: uppercase; line-height: 1;
  }
  .title-big { display: block; font-size: 82px; letter-spacing: 1px; }
  .title-small { display: block; font-size: 36px; margin: 6px 0 10px; letter-spacing: 0.5px; }
  .front-subtitle {
    position: absolute; left: 0; top: 620px; width: 557px; text-align: center;
    font-family: "Roboto Condensed", "Arial Narrow", sans-serif; font-weight: 700;
    font-size: 27px; line-height: 32px; color: var(--ink-white);
    text-shadow: 0 0 3px #000, 0 0 3px #000;
  }
  .author-band {
    position: absolute; left: 0; top: 742px; width: 557px; height: 38px;
    background: var(--band-white);
    font-family: "Oswald", "Arial Narrow", sans-serif; font-weight: 700;
    font-size: 31px; line-height: 38px; letter-spacing: 5px; text-align: center;
    color: var(--ink-black); text-transform: uppercase;
  }
</style>
</head>
<body>
<div class="canvas">

  <section class="back-cover">
    <div class="back-panel">
      <h2 class="back-heading">Readiness Beats Scrambling Through Wreckage</h2>
      <div class="back-copy">
        <p>Throughout history, women have always found themselves in an extraordinarily vulnerable position. Not least because, at the heart of family life, they often have the responsibility for bringing up and nurturing children.</p>
        <p>This book outlines a structured process by which women can avoid or reduce risk and uncertainty in their lives. It is written for women who have a lot to lose. Women, like you.</p>
        <p>In her professional life, the Author met countless women who, through no fault of their own, faced financial, physical and psychological distress because of redundancy, divorce, and critical illness. Some even lost their homes and were admitted to residential care. In every case, there were simple strategies that could have avoided or reduced the impact of these situations.</p>
        <p>You will discover how to make effective contingency plans in case your life does not work out exactly as you originally intended. You will discover how to reduce the risk of financial ruin, and the uncertain future it would create. The author takes you through the fundamentals steps for creating a contingency plan. You will be guided, step by step, through a process to set up a framework to safeguard your hard-earned assets and protect your loved ones from the risk of a future without basic necessities – food, water, clothing and a roof over your head.</p>
        <p class="lead">This book is brimming with tips and insightful case studies and covers every area of your life.</p>
        <ul class="topic-list">
          <li>Finance</li>
          <li>Relationships</li>
          <li>Health and Wellbeing</li>
          <li>Asset Ownership</li>
          <li>Family and Inheritance</li>
        </ul>
      </div>
      <p class="author-bio">Maren Ashby is a medical doctor and Member of the Guild of Family Physicians (UK). She has over twenty years’ experience and has worked in the National Care Service (NCS) and overseas missions. Maren has two children and has personally experienced the trauma of divorce; the impact of which was dire and could have been reduced if she had put some basic risk mitigation strategies in place beforehand. In getting through her own divorce, Maren learned some essential lessons for the future. Now she wants to share what she learned, so you don’t end up in the same dire situation.</p>
      <div class="author-photo" role="img" aria-label="Author portrait placeholder"></div>
      <div class="barcode-space"></div>
      <p class="website">www.bracingforstorms.co.uk</p>
    </div>
  </section>

  <section class="spine">
    <span class="spine-title">Bracing for Storms, Charting Every Exit</span>
    <span class="spine-author">Maren Ashby</span>
  </section>

  <section class="front-cover">
    <div class="cover-photo" role="img" aria-label="Photograph of a man seen from behind standing on a road at a fork, facing a signpost with arrows marked solution and problem, under a cloudy blue sky"></div>
    <h1 class="front-title">
      <span class="title-big">Bracing</span>
      <span class="title-small">For Storms</span>
      <span class="title-big">Charting</span>
      <span class="title-small">Every Exit</span>
    </h1>
    <p class="front-subtitle">Ways to build backup strategies<br>since readiness beats scrambling<br>through wreckage later</p>
    <div class="author-band">Maren Ashby</div>
  </section>

</div>
</body>
</html>
```